Business Card Design Project - 2 sided

We need a business card design for a card having one business on each side (ie. two businesses on one card). Would like a design that incorporates logo, tagline and normal fields (name, position, address, phone).

Would also like an allowance for small font text along the bottom (text to be determined, but less than 50 characters).

NB. Attached logo for Verbal Bridgeworks has two variations - either can be used.

www.verbalbridgeworks.com / www.kelpora.com

```html
<!DOCTYPE html>
<html lang="en">
<head>
<meta charset="utf-8">
<title>Two-sided business card – Kelpora / Verbal Bridgeworks</title>
<link rel="stylesheet" href="https://fonts.googleapis.com/css2?family=Open+Sans:wght@400;600;700&display=swap">
<style>
  :root {
    --bg: #e9e7e3;
    --card: #ffffff;
    --green: #7dc242;
    --green-light: #a9d86e;
    --navy: #2b2a7a;
    --blue: #2a7fc0;
    --ink: #333333;
    --muted: #6b6b6b;
    --photo-a: #c9b8a8;
    --photo-a2: #2c3447;
    --photo-b: #d9d9d9;
    --photo-b2: #6f6f78;
  }
  * { box-sizing: border-box; margin: 0; padding: 0; }
  html, body {
    width: 1200px; height: 900px; overflow: hidden;
    background: var(--bg);
    font-family: "Open Sans", Arial, sans-serif;
    color: var(--ink);
  }
  .canvas {
    width: 1200px; height: 900px;
    display: flex; flex-direction: column; align-items: center; justify-content: center; gap: 40px;
  }
  .card {
    position: relative; width: 680px; height: 388px;
    background: var(--card); overflow: hidden;
    box-shadow: 0 6px 18px rgba(0,0,0,.18);
  }
  .brand { position: absolute; display: flex; align-items: center; gap: 10px; }
  .brand-dot { width: 40px; height: 40px; border-radius: 50%; }
  .brand-name { font-weight: 700; }
  .tagline {
    position: absolute; font-size: 13px; color: var(--green);
    display: flex; align-items: baseline; gap: 4px;
  }
  .tagline::after {
    content: ""; width: 200px; border-bottom: 2px dotted var(--green);
  }
  .person-name { font-weight: 700; font-size: 19px; }
  .role { font-size: 13px; }
  .contacts { position: absolute; font-size: 13px; line-height: 1.5; }
  .contacts b { font-weight: 600; }
  .address { position: absolute; font-size: 12px; line-height: 1.45; }
  .text-info { position: absolute; font-size: 9px; line-height: 1.4; color: var(--muted); }
  .text-info b { color: var(--blue); font-weight: 600; }
  .photo { position: absolute; }

  /* Kelpora side */
  .kelpora .brand { left: 40px; top: 48px; }
  .kelpora .brand-dot { background: var(--green); }
  .kelpora .brand-name { font-size: 40px; color: var(--blue); letter-spacing: -1px; }
  .kelpora .tagline { left: 40px; top: 104px; }
  .kelpora .identity { position: absolute; left: 40px; top: 140px; }
  .kelpora .person-name { color: var(--blue); }
  .kelpora .contacts { left: 40px; top: 200px; }
  .kelpora .contacts b { color: var(--blue); }
  .kelpora .address { left: 318px; top: 222px; }
  .kelpora .photo {
    right: 0; top: 0; width: 300px; height: 210px;
    background: linear-gradient(160deg, var(--photo-a) 0%, #e9ded3 40%, var(--photo-a2) 80%);
  }
  .kelpora .text-info { left: 40px; top: 300px; width: 430px; }
  .kelpora .edge { position: absolute; inset: 0; }

  /* Verbal Bridgeworks side */
  .bridge .band {
    position: absolute; left: 0; top: 0; width: 100%; height: 52px;
    background: var(--green); display: flex; align-items: center; padding-left: 290px; gap: 10px;
  }
  .bridge .band::after {
    content: ""; position: absolute; left: 0; right: 0; bottom: -8px; height: 8px; background: var(--green-light);
  }
  .bridge .person-name { color: var(--navy); }
  .bridge .role { color: var(--navy); }
  .bridge .brand { left: 40px; top: 92px; }
  .bridge .brand-dot { background: var(--navy); }
  .bridge .brand-name { font-size: 28px; color: var(--navy); font-weight: 600; }
  .bridge .tagline { left: 40px; top: 142px; }
  .bridge .address { left: 40px; top: 176px; font-size: 13px; }
  .bridge .contacts { left: 40px; top: 222px; }
  .bridge .contacts b { color: var(--navy); }
  .bridge .text-info { left: 40px; top: 300px; width: 360px; }
  .bridge .photo {
    right: 0; top: 60px; width: 250px; height: 300px;
    background: linear-gradient(180deg, var(--photo-b) 0%, #eeeeee 35%, var(--photo-b2) 100%);
  }
  .bridge .base {
    position: absolute; left: 0; right: 0; bottom: 0; height: 28px; background: var(--navy);
  }
</style>
</head>
<body>
<main class="canvas">

  <section class="card kelpora" aria-label="Card side for Kelpora LLC">
    <svg class="edge" width="680" height="388" viewBox="0 0 680 388" aria-hidden="true">
      <polygon points="640,210 680,210 680,388 470,388" fill="#7dc242"/>
      <polygon points="664,210 680,210 680,388 650,388" fill="#2b2a7a"/>
    </svg>
    <div class="photo" role="img" aria-label="Photo of a smiling businesswoman giving a thumbs up"></div>
    <div class="brand">
      <span class="brand-dot"></span>
      <span class="brand-name">kelpora LLC</span>
    </div>
    <div class="tagline">tagline</div>
    <div class="identity">
      <div class="person-name">Clara Mendel</div>
      <div class="role">Manager</div>
    </div>
    <div class="contacts">
      <div><b>p:</b> +1 555 214 0186</div>
      <div><b>e:</b> support@kelpora.com</div>
      <div><b>w:</b> www.kelpora.com</div>
    </div>
    <div class="address">
      PO Box 42<br>Linden Vale Missouri 63000, USA<br>Orchard Lane<br>Bay Hollow Florida 34000, USA
    </div>
    <p class="text-info"><b>Text info:</b> Reaching every reader is never a simple task. There are many ways to say one thing, but choosing the best words takes skill and a little artful care, so your message truly lands.</p>
  </section>

  <section class="card bridge" aria-label="Card side for Verbal Bridgeworks">
    <div class="band">
      <span class="person-name">Clara Mendel</span>
      <span class="role">Manager</span>
    </div>
    <div class="photo" role="img" aria-label="Photo of a diverse group of business people"></div>
    <div class="brand">
      <span class="brand-dot"></span>
      <span class="brand-name">Verbal Bridgeworks</span>
    </div>
    <div class="tagline">tagline</div>
    <div class="address">27 Wren Street<br>Kelso VIC 3000, AUSTRALIA</div>
    <div class="contacts">
      <div><b>p:</b> +61 3 5550 1427</div>
      <div><b>e:</b> info@verbalbridgeworks.com</div>
      <div><b>w:</b> www.verbalbridgeworks.com</div>
    </div>
    <p class="text-info"><b>Text info:</b> Reaching every reader is never a simple task. There are many ways to say one thing, but choosing the best words takes skill and a little artful care, so your message truly lands.</p>
    <div class="base"></div>
  </section>

</main>
</body>
</html>
```